Website Design for PawRank - New Digital Agency

We are creating a new digital marketing agency and need a new website. I have attached the logo. Our niche is going to be veterinarians. Use the same colors as in the logo (blue, white and gray).

I want real pictures of real people in this and not just boring stock photos. It needs to be related to the industry.

Home page (example:https://trellmarsh.com/)
Service page (example: https://dovequist.com/consulting/)
Case study page (example: https://www.harlowfinchley.com/seo/case-study/)

I will continue to update this brief.
Updates

I updated the brief with some additional sample sites 2 days ago and want to see more designs. I won't need that may more days ...just a few more.

Target Market(s)

veterinarians

Font styles to use
Sans Serif

Requirements
Must have
• I want a very clean looking site. Use the same colors as in the logo (blue, white and gray).
Nice to have
• We need to build this with the idea that the purpose is to generate leads for our business.
• Home page (example:https://trellmarsh.com/)
• Service page (example: https://dovequist.com/consulting/)
• Case study page (example: https://www.harlowfinchley.com/seo/case-study/)

```html
<!DOCTYPE html>
<html lang="en">
<head>
<meta charset="utf-8">
<title>PawRank — Digital Marketing for Veterinarians</title>
<link href="https://fonts.googleapis.com/css2?family=Montserrat:wght@400;500;600;700;800&family=Lato:ital,wght@0,400;0,700;0,900;1,400&display=swap" rel="stylesheet">
<style>
:root{
  --blue:#1c57a5;
  --blue-dark:#163f7a;
  --navy:#1a3c6e;
  --ink:#111;
  --text:#555;
  --gray-bg:#ececec;
  --footer:#1c1c1c;
  --white:#fff;
}
*{margin:0;padding:0;box-sizing:border-box}
html,body{width:1200px;height:3651px;overflow:hidden}
body{position:relative;background:var(--white);font-family:'Lato',sans-serif;color:var(--text)}
.abs{position:absolute}
a{color:inherit;text-decoration:none}

/* header */
.site-header{position:absolute;left:0;top:0;width:1200px;height:74px;background:var(--white);z-index:5}
.brand{position:absolute;display:flex;align-items:center;gap:8px;font-family:'Montserrat',sans-serif;font-weight:700;color:var(--blue)}
.brand .dot{width:22px;height:22px;border-radius:50%;background:var(--blue)}
.site-header .brand{left:173px;top:18px;font-size:34px}
.nav{position:absolute;top:29px;font-family:'Montserrat',sans-serif;font-weight:600;font-size:12px;color:#222}
.signup{position:absolute;left:963px;top:21px;width:76px;height:33px;background:var(--blue);color:#fff;border-radius:3px;font:700 13px 'Lato',sans-serif;display:flex;align-items:center;justify-content:center}

/* hero */
.hero{position:absolute;left:0;top:74px;width:1200px;height:634px;background:linear-gradient(180deg,#3b78c4 0%,#5b8fcf 35%,#a9c3e6 70%,#fafafa 100%);overflow:hidden}
.hero-title{position:absolute;left:163px;top:200px;font-family:'Montserrat',sans-serif;font-weight:800;font-size:70px;line-height:76px;color:var(--ink)}
.hero-sub{position:absolute;left:163px;top:373px;font-size:18px;color:#fff}
.btn{position:absolute;background:var(--blue);color:#fff;font:900 15px 'Lato',sans-serif;display:flex;align-items:center;justify-content:center;border-radius:2px}
.slider-dots .ring{position:absolute;left:53px;width:18px;height:18px;border:1.5px solid #222;border-radius:50%}
.slider-dots .ring.on::after{content:"";position:absolute;left:3px;top:3px;width:9px;height:9px;border-radius:50%;background:#222}

/* sections */
.eyebrow{position:absolute;display:flex;align-items:center;gap:8px;font-size:12px;color:#555}
.eyebrow i{width:20px;height:20px;border-radius:50%;background:var(--blue);display:block}
.eyebrow.light{color:#fff}
.eyebrow.light i{background:#fff}
.h2{position:absolute;font-family:'Montserrat',sans-serif;font-weight:500;font-size:31px;color:var(--navy)}
.center{left:0;width:1200px;text-align:center}
.center.eyebrow{justify-content:center}

.services{position:absolute;left:0;top:708px;width:1200px;height:475px;background:linear-gradient(180deg,#f9f9f9,#e7e7e7)}
.svc{position:absolute;width:260px;text-align:center}
.svc .icon{width:88px;height:88px;margin:0 auto;border-radius:50%;background:#fff;border:1px solid #ddd;display:flex;align-items:center;justify-content:center}
.svc .icon.active{background:var(--blue-dark);border-color:var(--blue-dark)}
.svc h3{margin-top:22px;font:500 15px 'Montserrat',sans-serif;color:#222}
.svc p{margin-top:14px;font-size:11.5px;line-height:19.5px;color:#666}
.svc a{display:block;margin-top:20px;font:700 11.5px 'Lato',sans-serif;color:#222;text-decoration:underline}

.about-title{position:absolute;left:612px;top:1285px;font:500 33px/38px 'Montserrat',sans-serif;color:var(--blue-dark)}
.about-text{position:absolute;left:612px;top:1425px;width:430px;font-size:11.5px;line-height:19.5px;color:#666}

.why{position:absolute;left:0;top:1783px;width:1200px;height:435px;background:linear-gradient(160deg,#1e4a83 0%,#2a5a98 45%,#1f4c8a 100%)}
.why-card{position:absolute;width:277px;height:84px;background:#fff;display:flex;align-items:center;padding:0 12px;gap:14px}
.why-card svg{flex:none}
.why-card h4{font:900 13px 'Lato',sans-serif;color:#111}
.why-card h4.accent{color:var(--blue)}
.why-card p{margin-top:4px;font-size:11px;line-height:19px;color:#666}

.quote-text{position:absolute;left:215px;top:2447px;width:375px;font-style:italic;font-size:12.5px;line-height:22.6px;color:#555}

.blog-card{position:absolute;width:277px;height:323px;background:#fff;box-shadow:0 1px 6px rgba(0,0,0,.18)}
.blog-card .ph{height:188px}
.blog-card h4{margin:16px 13px 0;font:900 13.5px 'Lato',sans-serif;color:#111}
.blog-card p{margin:6px 13px 0;font-size:11px;line-height:19px;color:#666}
.blog-card a{display:flex;align-items:center;gap:8px;margin:12px 13px 0;font:900 11.5px 'Lato',sans-serif;color:var(--blue);text-decoration:underline}

.cta{position:absolute;left:0;top:3237px;width:1200px;height:76px;background:var(--blue)}
.cta p{position:absolute;left:163px;top:22px;font:500 27px 'Montserrat',sans-serif;color:#fff}
.cta .btn{left:925px;top:19px;width:114px;height:40px;background:#fff;color:var(--blue);border-radius:3px}

.footer{position:absolute;left:0;top:3313px;width:1200px;height:338px;background:var(--footer)}
.footer .brand{left:161px;top:30px;font-size:38px}
.f-about{position:absolute;left:161px;top:106px;width:200px;font-size:11.5px;line-height:19.5px;color:#ddd}
.f-head{position:absolute;top:60px;font:700 13px 'Lato',sans-serif;color:var(--blue)}
.f-list{position:absolute;left:388px;top:94px;list-style:none;font-size:11.5px;line-height:19.6px;color:#eee}
.f-item{position:absolute;left:650px;font-size:11.5px;line-height:18px;color:#eee}
.social{position:absolute;top:3519px;width:36px;height:36px;border-radius:50%;background:var(--blue)}
.sub-input{position:absolute;left:837px;top:3413px;width:160px;height:44px;background:#fff;font-style:italic;font-size:11px;color:#999;padding:15px 8px}
.sub-btn{position:absolute;left:995px;top:3413px;width:44px;height:44px;background:var(--blue);display:flex;align-items:center;justify-content:center}
.copyright{position:absolute;left:0;top:3617px;width:1200px;text-align:center;font-size:11.5px;color:#ddd}
.copyright b{color:#fff}
</style>
</head>
<body>

<header class="site-header">
  <div class="brand"><span>PawRank</span><span class="dot"></span></div>
  <nav>
    <a class="nav" style="left:599px">Home</a>
    <a class="nav" style="left:655px">About</a>
    <a class="nav" style="left:711px">Services</a>
    <a class="nav" style="left:779px">Contact</a>
  </nav>
  <svg class="abs" style="left:884px;top:28px" width="20" height="20" viewBox="0 0 20 20"><circle cx="8" cy="8" r="6" fill="none" stroke="#999" stroke-width="2"/><line x1="12.5" y1="12.5" x2="18" y2="18" stroke="#999" stroke-width="2"/></svg>
  <a class="signup">Sign Up</a>
</header>

<section class="hero">
  <svg class="abs" style="left:0;top:0" width="1200" height="634">
    <defs>
      <linearGradient id="heroPhoto" x1="0" y1="0" x2="1" y2="1"><stop offset="0" stop-color="#5b4a3c"/><stop offset=".5" stop-color="#cbb9a5"/><stop offset="1" stop-color="#e8dfd3"/></linearGradient>
    </defs>
    <circle cx="90" cy="-20" r="85" fill="#2f67b2" opacity=".6"/>
    <circle cx="330" cy="-25" r="95" fill="#2f67b2" opacity=".5"/>
    <circle cx="590" cy="-20" r="90" fill="#2f67b2" opacity=".5"/>
    <circle cx="840" cy="-30" r="95" fill="#2f67b2" opacity=".45"/>
    <g role="img" aria-label="Photo of a smiling woman in glasses holding a phone">
      <rect x="640" y="235" width="640" height="300" rx="150" fill="url(#heroPhoto)" transform="rotate(-42 960 385)"/>
    </g>
    <circle cx="1210" cy="265" r="55" fill="#4d86cc"/>
  </svg>
  <div class="slider-dots">
    <svg class="abs" style="left:53px;top:207px" width="20" height="12"><polyline points="2,10 10,2 18,10" fill="none" stroke="#222" stroke-width="1.5"/></svg>
    <span class="ring" style="top:254px"></span>
    <span class="ring on" style="top:291px"></span>
    <span class="ring" style="top:329px"></span>
    <span class="ring" style="top:366px"></span>
    <svg class="abs" style="left:53px;top:422px" width="20" height="12"><polyline points="2,2 10,10 18,2" fill="none" stroke="#222" stroke-width="1.5"/></svg>
  </div>
  <h1 class="hero-title">Let's Start<br>Work Together</h1>
  <p class="hero-sub">Provide all kinds of seo services and help.</p>
  <a class="btn" style="left:161px;top:436px;width:135px;height:44px">Explore More</a>
</section>

<section class="services">
  <div class="eyebrow center" style="top:38px"><i></i>Our Services</div>
  <h2 class="h2 center" style="top:68px">Discover services we’r provided</h2>
  <svg class="abs" style="left:0;top:202px" width="1200" height="2"><line x1="343" y1="1" x2="555" y2="1" stroke="#ccc"/><line x1="643" y1="1" x2="856" y2="1" stroke="#ccc"/></svg>
  <div class="svc" style="left:169px;top:158px">
    <div class="icon"><svg width="46" height="46" viewBox="0 0 46 46" fill="none" stroke="#1c3f73" stroke-width="1.6"><rect x="10" y="6" width="20" height="32" rx="2"/><circle cx="18" cy="14" r="6"/><text x="15" y="18" font-size="10" fill="#1c3f73" stroke="none">$</text><rect x="26" y="28" width="12" height="10"/></svg></div>
    <h3>Paid Media</h3>
    <p>Lorem Ipsum is simply dummy text of the printing and typesetting industry. Lorem Ipsum has been the industry's standard dummy text ever since the 1500s</p>
    <a>Learn More</a>
  </div>
  <div class="svc" style="left:469px;top:158px">
    <div class="icon active"><svg width="46" height="46" viewBox="0 0 46 46" fill="none" stroke="#fff" stroke-width="1.8"><rect x="6" y="9" width="34" height="26" rx="2"/><line x1="6" y1="15" x2="40" y2="15"/><polyline points="18,20 14,24 18,28"/><polyline points="28,20 32,24 28,28"/></svg></div>
    <h3>Content Marketing Management</h3>
    <p>Lorem Ipsum is simply dummy text of the printing and typesetting industry. Lorem Ipsum has been the industry's standard dummy text ever since the 1500s</p>
    <a>Learn More</a>
  </div>
  <div class="svc" style="left:770px;top:158px">
    <div class="icon"><svg width="46" height="46" viewBox="0 0 46 46" fill="none" stroke="#1c3f73" stroke-width="1.6"><rect x="5" y="7" width="36" height="26" rx="2"/><polyline points="11,26 18,18 25,22 34,13"/><line x1="23" y1="33" x2="23" y2="39"/><line x1="15" y1="39" x2="31" y2="39"/></svg></div>
    <h3>Digital Services</h3>
    <p>Lorem Ipsum is simply dummy text of the printing and typesetting industry. Lorem Ipsum has been the industry's standard dummy text ever since the 1500s</p>
    <a>Learn More</a>
  </div>
</section>

<section class="about">
  <svg class="abs" style="left:0;top:1236px" width="600" height="472">
    <defs><linearGradient id="aboutPhoto" x1="0" y1="0" x2="1" y2="1"><stop offset="0" stop-color="#3f4f68"/><stop offset=".6" stop-color="#27354b"/><stop offset="1" stop-color="#1a2434"/></linearGradient></defs>
    <g role="img" aria-label="Video still of a veterinarian holding a puppy">
      <rect x="-160" y="60" width="800" height="360" rx="180" fill="url(#aboutPhoto)" transform="rotate(-38 240 240)"/>
    </g>
    <rect x="-140" y="290" width="300" height="110" rx="55" fill="#fff" transform="rotate(-38 10 345)"/>
    <circle cx="326" cy="206" r="37" fill="none" stroke="#fff" stroke-width="3"/>
    <polygon points="314,186 314,226 344,206" fill="#fff"/>
  </svg>
  <div class="eyebrow" style="left:612px;top:1256px"><i></i>About Us</div>
  <h2 class="about-title">We’ve skill in wide range of<br>web and Other digital<br>market tools.</h2>
  <p class="about-text">Lorem Ipsum is simply dummy text of the printing and typesetting industry. Lorem Ipsum has been the industry's standard dummy text ever since the 1500s, when an unknown printer took a galley of type and scrambled it to make a type specimen book.</p>
  <a class="btn" style="left:611px;top:1549px;width:112px;height:40px;font-size:14px">Learn More</a>
</section>

<section class="why" role="img" aria-label="Background photo of a dog in a field under a blue overlay">
  <div class="eyebrow light center" style="top:44px"><i></i>Why Us?</div>
  <h2 class="h2 center" style="top:80px;color:#fff">We complete every step carefully</h2>
</section>
<div class="why-card" style="left:161px;top:1938px">
  <svg width="40" height="40" viewBox="0 0 40 40" fill="none" stroke="#777" stroke-width="1.5"><circle cx="8" cy="8" r="5"/><circle cx="32" cy="8" r="5"/><circle cx="20" cy="20" r="5"/><circle cx="8" cy="32" r="5"/><circle cx="32" cy="32" r="5"/></svg>
  <div><h4>Relevant, Powerful Links</h4><p>Lorem Ipsum is simply dummy text of the printing and typesetting industry.</p></div>
</div>
<div class="why-card" style="left:462px;top:1940px">
  <svg width="40" height="40" viewBox="0 0 40 40" fill="none" stroke="#1c57a5" stroke-width="1.6"><rect x="3" y="7" width="34" height="26"/><polyline points="8,27 15,19 21,23 31,13"/></svg>
  <div><h4 class="accent">Only White Hat Strategies</h4><p>Lorem Ipsum is simply dummy text of the printing and typesetting industry.</p></div>
</div>
<div class="why-card" style="left:761px;top:1938px">
  <svg width="40" height="40" viewBox="0 0 40 40" fill="none" stroke="#666" stroke-width="1.6"><path d="M4 18 L12 12 L20 16 L28 12 L36 18 L24 30 Q20 32 16 28 Z"/></svg>
  <div><h4>100% Satisfaction</h4><p>Lorem Ipsum is simply dummy text of the printing and typesetting industry.</p></div>
</div>
<div class="why-card" style="left:312px;top:2042px">
  <svg width="40" height="40" viewBox="0 0 40 40" fill="none" stroke="#777" stroke-width="1.5"><rect x="6" y="16" width="28" height="18"/><circle cx="20" cy="10" r="6"/><line x1="6" y1="22" x2="34" y2="22"/></svg>
  <div><h4>Reduce Operational Costs</h4><p>Lorem Ipsum is simply dummy text of the printing and typesetting industry.</p></div>
</div>
<div class="why-card" style="left:611px;top:2042px">
  <svg width="40" height="40" viewBox="0 0 40 40" fill="none" stroke="#555" stroke-width="1.6"><circle cx="22" cy="18" r="13"/><text x="14" y="23" font-size="12" fill="#555" stroke="none" font-family="Lato">24</text><path d="M4 22 Q6 34 16 36"/></svg>
  <div><h4>World-class Customer Support</h4><p>Lorem Ipsum is simply dummy text of the printing and typesetting industry.</p></div>
</div>

<section class="testimonials">
  <div class="eyebrow" style="left:163px;top:2295px"><i></i>Testimonials</div>
  <h2 class="h2" style="left:163px;top:2325px;line-height:38px">Check what our client<br>Says about us</h2>
  <svg class="abs" style="left:161px;top:2430px" width="44" height="40"><polygon points="0,0 18,0 18,26 6,38 6,26 0,26" fill="#1c57a5"/><polygon points="24,0 42,0 42,26 30,38 30,26 24,26" fill="#1c57a5"/></svg>
  <p class="quote-text">Lorem Ipsum is simply dummy text of the printing and typesetting industry. Lorem Ipsum has been the industry's standard dummy text ever since the 1500s, when an unknown printer took a galley of type and scrambled it to make a type specimen book.</p>
  <p class="abs" style="left:215px;top:2560px;font-size:11.5px;color:#222">- John Doe</p>
  <svg class="abs" style="left:498px;top:2560px" width="64" height="16" fill="#1c57a5" stroke="#1c57a5" stroke-width="2.5"><line x1="4" y1="8" x2="28" y2="8"/><polygon points="0,8 9,2 9,14" stroke="none"/><line x1="36" y1="8" x2="58" y2="8"/><polygon points="64,8 55,2 55,14" stroke="none"/></svg>
  <svg class="abs" style="left:620px;top:2240px" width="580" height="440">
    <defs><linearGradient id="testiPhoto" x1="0" y1="0" x2="1" y2="1"><stop offset="0" stop-color="#d8d0c6"/><stop offset=".5" stop-color="#8a7a6c"/><stop offset="1" stop-color="#ece6de"/></linearGradient></defs>
    <g role="img" aria-label="Photo of a veterinarian examining a spaniel with a stethoscope">
      <rect x="-10" y="90" width="600" height="290" rx="145" fill="url(#testiPhoto)" transform="rotate(-40 290 235)"/>
    </g>
    <rect x="380" y="10" width="240" height="70" rx="35" fill="#fff" transform="rotate(-40 500 45)"/>
  </svg>
</section>

<section class="blog">
  <svg class="abs" style="left:0;top:2880px" width="1200" height="200" fill="none" stroke="#1c57a5" stroke-width="1">
    <path d="M0 140 Q60 170 130 159"/><path d="M1039 49 Q1120 40 1200 90"/>
    <circle cx="130" cy="159" r="7" fill="#fff"/><circle cx="1068" cy="49" r="7" fill="#fff"/>
  </svg>
  <div class="eyebrow center" style="top:2730px"><i></i>Our Blog</div>
  <h2 class="h2 center" style="top:2762px">Blog from our company</h2>
  <article class="blog-card" style="left:161px;top:2848px">
    <div class="ph" role="img" aria-label="Photo of vets examining a small white dog" style="background:linear-gradient(135deg,#e9e4dc,#b9a690)"></div>
    <h4>Lorem ipsum is simply dummy</h4>
    <p>Lorem Ipsum is simply dummy text of the printing and typesetting industry.</p>
    <a>Learn More <svg width="20" height="10" fill="#1c57a5"><rect y="4" width="14" height="2"/><polygon points="20,5 13,0 13,10"/></svg></a>
  </article>
  <article class="blog-card" style="left:462px;top:2848px">
    <div class="ph" role="img" aria-label="Photo of a shepherd dog in warm light" style="background:linear-gradient(135deg,#d48a3e,#6b4a2e)"></div>
    <h4>Lorem ipsum is simply dummy.</h4>
    <p>Lorem Ipsum is simply dummy text of the printing and typesetting industry.</p>
    <a>Learn More <svg width="20" height="10" fill="#1c57a5"><rect y="4" width="14" height="2"/><polygon points="20,5 13,0 13,10"/></svg></a>
  </article>
  <article class="blog-card" style="left:761px;top:2848px">
    <div class="ph" role="img" aria-label="Black and white photo of a dog in profile" style="background:linear-gradient(135deg,#8a8a8a,#1a1a1a)"></div>
    <h4>Lorem ipsum is simply dummy</h4>
    <p>Lorem Ipsum is simply dummy text of the printing and typesetting industry.</p>
    <a>Learn More <svg width="20" height="10" fill="#1c57a5"><rect y="4" width="14" height="2"/><polygon points="20,5 13,0 13,10"/></svg></a>
  </article>
</section>

<section class="cta">
  <p>Any Queries? Don’t Hesitate? Feel Free to Make a Call</p>
  <a class="btn">Contact US</a>
</section>

<footer class="footer">
  <div class="brand"><span>PawRank</span><span class="dot"></span></div>
  <p class="f-about">Lorem Ipsum is simply dummy text of the printing and typesetting industry. Lorem Ipsum has been the industry's standard dummy text.</p>
  <h5 class="f-head" style="left:388px">Quick Link</h5>
  <ul class="f-list"><li>Home</li><li>About us</li><li>Servcies</li><li>Blog</li><li>Testiminials</li><li>Contact Us</li></ul>
  <h5 class="f-head" style="left:612px">Contact Info</h5>
  <svg class="abs" style="left:612px;top:96px" width="22" height="120" fill="none" stroke="#1c57a5" stroke-width="2">
    <path d="M4 4 Q4 16 16 18 L18 14 L14 11 L12 13 Q8 11 7 7 L9 5 L6 1 Z"/>
    <rect x="2" y="44" width="18" height="13"/><polyline points="2,44 11,52 20,44"/>
    <path d="M11 104 Q3 94 3 89 A8 8 0 0 1 19 89 Q19 94 11 104 Z"/><circle cx="11" cy="89" r="3"/>
  </svg>
  <p class="f-item" style="top:96px">+91-000-000-0000</p>
  <p class="f-item" style="top:137px">hello@pawrank.com</p>
  <p class="f-item" style="top:180px;width:160px">100 - Lorem Ipsum is simply dummy text of the printing .</p>
  <h5 class="f-head" style="left:837px">Subscribe Now</h5>
</footer>
<div class="sub-input">Enter Email</div>
<div class="sub-btn"><svg width="10" height="14" fill="none" stroke="#fff" stroke-width="2"><polyline points="2,2 8,7 2,12"/></svg></div>
<span class="social" style="left:162px"></span>
<span class="social" style="left:207px"></span>
<span class="social" style="left:251px"></span>
<span class="social" style="left:297px"></span>
<svg class="abs" style="left:161px;top:3600px" width="880" height="2"><line x1="0" y1="1" x2="878" y2="1" stroke="#555"/></svg>
<p class="copyright">Copyright © 2018 By <b>PawRank</b>. All Rights Reserved. Terms and Conditions.</p>

</body>
</html>
```